New Word Template Design Project

I need this document for death certificate ordering to look like our branding. I will attach the pdf with the information and a sample pdf of our style. I also think that check boxes and x's would be better than yes and no.

2nd page in spanish.

Industry/Entity Type

Funeral

Requirements
Should not have
• Check boxes and red x's or yellow next to the yes, no , or sometimes

```html
<!DOCTYPE html>
<html lang="en">
<head>
<meta charset="utf-8">
<title>Hartwell – Pre-Planning Checklist &amp; Certificate Guide</title>
<link rel="stylesheet" href="https://fonts.googleapis.com/css2?family=Montserrat:wght@700;800&family=Nunito+Sans:ital,wght@0,400;0,600;0,700;1,700&display=swap">
<style>
  :root{
    --stage:#2d2d2d;
    --paper:#ffffff;
    --brand:#4c7d9c;
    --brand-dark:#3f6d8a;
    --ink:#333a40;
    --muted:#6b7075;
    --field:#878787;
    --box:#8c8c8c;
    --rule:#c9ced2;
  }
  *{box-sizing:border-box;margin:0;padding:0}
  html,body{width:1200px;height:1200px;overflow:hidden;background:var(--stage)}
  body{font-family:"Nunito Sans",Arial,sans-serif;color:var(--ink);position:relative}

  .page{position:absolute;top:237px;width:560px;height:725px;background:var(--paper);overflow:hidden}
  .page--checklist{left:20px}
  .page--guide{left:620px}

  .band{position:absolute;top:52px;height:20px;background:var(--brand)}
  .band--title{left:0;width:376px;display:flex;align-items:center;padding-left:36px}
  .band--end{right:0;width:32px}
  .band--title h1{font-family:Montserrat,Arial,sans-serif;font-weight:800;font-size:15px;color:#fff;letter-spacing:.2px;white-space:nowrap}
  .page--guide .band--title{width:378px;padding-left:36px}
  .page--guide .band--title h1{font-size:12.6px}

  .brand{position:absolute;left:388px;top:38px;width:140px;text-align:center}
  .brand__name{display:flex;align-items:center;justify-content:center;gap:5px;font-family:"Nunito Sans",Arial,sans-serif;font-weight:700;font-size:25px;color:var(--brand);line-height:1}
  .brand__dot{width:8px;height:8px;border-radius:50%;background:var(--brand)}
  .brand__line{font-size:5px;letter-spacing:1.6px;color:var(--brand);margin-top:6px;font-weight:700}
  .brand__tag{font-size:4.8px;font-style:italic;color:var(--muted);margin-top:3px}

  .content{position:absolute;left:37px;right:37px;top:109px}
  .sec{margin-top:6px}
  .sec__head{display:flex;align-items:center;gap:6px;height:14px}
  .sec__head h2{font-family:"Nunito Sans",Arial,sans-serif;font-weight:700;font-size:8.6px;color:var(--brand);white-space:nowrap;letter-spacing:.2px}
  .sec__head::after{content:"";flex:1;height:1.5px;background:var(--brand)}

  .row{display:flex;align-items:center;height:12.7px;font-size:6.6px;white-space:nowrap}
  .lbl{flex:none}
  .bar{flex:1;height:8px;background:var(--field);margin-left:5px}
  .w48{width:48px}.w122{width:122px}.w102{width:102px}.w64{width:64px}
  .tall{height:17px;line-height:1.1}
  .tall small{font-size:4.6px;display:block}

  .cols{display:grid;grid-template-columns:295px 1fr;column-gap:9px}
  .dob{display:flex;gap:4px;margin-left:5px}
  .dob span{display:flex}
  .dob i{width:8px;height:8px;border:.8px solid var(--box)}

  .opts{display:grid;grid-template-columns:168px 85px 93px 76px 1fr;align-items:center;height:12.7px;font-size:6.6px;white-space:nowrap}
  .cb{display:inline-flex;align-items:center;gap:6px}
  .cb::before{content:"";width:7px;height:7px;border:.8px solid var(--box);border-radius:1px;flex:none}

  .closing{position:absolute;left:37px;right:37px;top:686px;font-size:7px;font-style:italic;font-weight:700;color:var(--brand)}

  .tag{display:inline-block;background:var(--brand);color:#fff;font-size:6.6px;font-weight:700;padding:1px 5px;margin-top:3px}
  .para{font-size:6.6px;line-height:1.45;margin-top:9px}
  .para b{font-weight:700}
  table.uses{width:487px;border-collapse:collapse;margin-top:8px;font-size:6.6px;border:.8px solid var(--rule)}
  .uses th{background:var(--brand);color:#fff;font-weight:600;text-align:left;height:13px;padding-left:5px}
  .uses td{height:14.4px;padding-left:5px;border-bottom:.8px solid var(--rule)}
  .uses col.c1{width:195px}.uses col.c2{width:120px}.uses col.c3{width:85px}
  .sub{font-weight:700;font-size:8.2px;color:var(--brand);margin-top:10px}
  .sub + .para{margin-top:1px}
  .blanks{font-size:6.6px;line-height:1.6;margin-top:2px}
  .contact{display:grid;grid-template-columns:230px 1fr;margin-top:3px}
  .contact__list{font-size:6.6px;line-height:1.6}
  .contact__phone{display:flex;align-items:center;gap:6px;font-weight:700}
  .contact__mail{display:flex;gap:6px;margin-top:1px}
  .contact__mail ul{list-style:none;border-left:.8px solid var(--muted);padding-left:7px}
  .contact__line{font-size:9px;font-style:italic;font-weight:700;color:var(--brand);line-height:1.35;align-self:center;padding-top:6px}
  svg{flex:none}
</style>
</head>
<body>

<section class="page page--checklist">
  <div class="band band--title"><h1>PRE-PLANNING FUNERAL CHECKLIST</h1></div>
  <div class="band band--end"></div>
  <div class="brand">
    <div class="brand__name"><span class="brand__dot"></span>Hartwell</div>
    <div class="brand__line">FUNERAL &amp; CREMATION SERVICES</div>
    <div class="brand__tag">Honoring Families Since 1931</div>
  </div>

  <div class="content">
    <div class="sec" style="margin-top:0">
      <div class="sec__head"><h2>PERSONAL INFORMATION</h2></div>
      <div class="cols">
        <div>
          <div class="row"><span class="lbl w48">Full name</span><span class="bar"></span></div>
          <div class="row"><span class="lbl w48">Address</span><span class="bar"></span></div>
          <div class="row tall"><span class="lbl w122">Military service information<small>(if applicable)</small></span><span class="bar"></span></div>
          <div class="row"><span class="lbl w122">Occupation and industry</span><span class="bar"></span></div>
          <div class="row tall"><span class="lbl w122">Spouse and children's names<br>and contact information</span><span class="bar"></span></div>
        </div>
        <div>
          <div class="row"><span class="lbl w102">Date of birth (DD/MM/YY)</span>
            <span class="dob"><span><i></i><i></i></span><span><i></i><i></i></span><span><i></i><i></i><i></i><i></i></span></span></div>
          <div class="row"><span class="lbl w102">Social security number</span><span class="bar"></span></div>
          <div class="row"><span class="lbl w102">City, state, and country of birth</span><span class="bar"></span></div>
          <div class="row"><span class="lbl w64">Father's full name</span><span class="bar"></span></div>
          <div class="row tall"><span class="lbl w64">Mother's full name<small>(including maiden name)</small></span><span class="bar"></span></div>
        </div>
      </div>
    </div>

    <div class="sec">
      <div class="sec__head"><h2>FUNERAL PREFERENCES</h2></div>
      <div class="row"><span class="lbl">Burial or cremation preferences</span><span class="bar"></span></div>
      <div class="opts"><span>Type of service</span><span class="cb">Traditional</span><span class="cb">Cremation</span><span class="cb">Green burial</span><span class="cb">Memorial</span></div>
      <div class="opts"><span>Preferred funeral location</span><span class="cb">Home</span><span class="cb">Church</span><span class="cb">Funeral home</span><span></span></div>
      <div class="opts"><span>Officiant preferences</span><span class="cb">Clergy</span><span class="cb">Celebrant</span><span class="cb">Family member</span><span></span></div>
      <div class="row"><span class="lbl">Type of casket or urn (if applicable)</span><span class="bar"></span></div>
      <div class="opts"><span>Special requests</span><span class="cb">Eco-friendly</span><span class="cb">Specific rituals</span><span class="cb">Ceremonies</span><span></span></div>
    </div>

    <div class="sec">
      <div class="sec__head"><h2>SERVICE DETAILS</h2></div>
      <div class="opts"><span>Desired location for the service</span><span class="cb">Church</span><span class="cb">Cemetery</span><span class="cb">Funeral</span><span class="cb">Home</span></div>
      <div class="row"><span class="lbl">Specific music or readings to be included</span><span class="bar"></span></div>
      <div class="opts"><span>Special tributes or memorials</span><span class="cb">Video tributes</span><span class="cb">Photos</span><span class="cb" style="grid-column:4 / 6">30-50 Pictures for video tribute</span></div>
      <div class="row"><span class="lbl">Pallbearers or special participants in the service</span><span class="bar"></span></div>
      <div class="opts"><span>Clothing and personal items for the deceased</span><span class="cb">For viewings</span><span class="cb">Burial</span><span></span><span></span></div>
      <div class="opts"><span>Obituary details</span><span class="cb">Draft of obituary</span><span class="cb">Key points to include</span><span></span><span></span></div>
      <div class="opts"><span>Livestream service: Should the service be livestreamed?</span><span></span><span class="cb">Yes</span><span class="cb">No</span><span></span></div>
    </div>

    <div class="sec">
      <div class="sec__head"><h2>CREMATION AND BURIAL DETAILS (IF APPLICABLE)</h2></div>
      <div class="row"><span class="lbl">Type of urn (if cremation is chosen)</span><span class="bar"></span></div>
      <div class="row"><span class="lbl">Cemetery or burial location preferences</span><span class="bar"></span></div>
      <div class="opts"><span>Grave marker or headstone preferences</span><span class="cb">Design</span><span class="cb">Inscription</span><span></span><span></span></div>
      <div class="opts"><span>Special requests for memorialization</span><span class="cb">Hearth stones</span><span class="cb">Lumera diamonds</span><span class="cb">Coralis reefs</span><span class="cb">Keepsake prints</span></div>
    </div>

    <div class="sec">
      <div class="sec__head"><h2>LEGAL AND FINANCIAL CONSIDERATIONS</h2></div>
      <div class="row"><span class="lbl">Pre-planned funeral agreement number</span><span class="bar"></span></div>
      <div class="row"><span class="lbl">Life insurance or other assets to cover funeral expenses</span><span class="bar"></span></div>
      <div class="opts"><span>Specific instructions for handling final expenses</span><span class="cb">Funding sources</span><span class="cb">Trusts</span><span></span><span></span></div>
      <div class="row"><span class="lbl">Identifying next of kin for funeral arrangements</span><span class="bar"></span></div>
    </div>

    <div class="sec">
      <div class="sec__head"><h2>DOCUMENTS AND ARRANGEMENTS</h2></div>
      <div class="opts"><span>Location of important documents</span><span class="cb">Will</span><span class="cb">Life insurance policies</span><span class="cb" style="grid-column:4 / 6">Pre-need funeral plan</span></div>
      <div class="row"><span class="lbl">Contact information for the estate planning attorney or financial advisor</span><span class="bar"></span></div>
      <div class="row"><span class="lbl">Funeral home contact information</span><span class="bar"></span></div>
      <div class="row"><span class="lbl">Special instructions (donations to charity, organ donation preferences, etc.)</span><span class="bar"></span></div>
    </div>

    <div class="sec">
      <div class="sec__head"><h2>OTHER PERSONAL WISHES</h2></div>
      <div class="row"><span class="lbl">Special requests for memorial services or receptions (location, food, theme, etc.)</span><span class="bar"></span></div>
      <div class="opts"><span>Personal messages or letters to loved ones to be read during the service</span><span></span><span class="cb"></span><span></span><span></span></div>
      <div class="opts"><span>Specific requests for the scattering of ashes</span><span></span><span class="cb">Location</span><span class="cb">Ceremony</span><span></span></div>
    </div>
  </div>

  <p class="closing">By making your wishes known in advance, you provide comfort and clarity for your family, helping them navigate a difficult time with ease.</p>
</section>

<section class="page page--guide">
  <div class="band band--title"><h1>HARTWELL FUNERAL &amp; CREMATION SERVICES</h1></div>
  <div class="band band--end"></div>
  <div class="brand">
    <div class="brand__name"><span class="brand__dot"></span>Hartwell</div>
    <div class="brand__line">FUNERAL &amp; CREMATION SERVICES</div>
    <div class="brand__tag">Honoring Families Since 1931</div>
  </div>

  <div class="content">
    <div class="sec__head" style="width:486px"><h2>GUÍA PARA SOLICITAR CERTIFICADOS DE DEFUNCIÓN</h2></div>
    <span class="tag">Condado de Miami-Dade</span>
    <p class="para">Los certificados de defunción certificados se utilizan para manejar asuntos legales, financieros y personales después del fallecimiento de un ser querido. Algunas instituciones requieren el original, mientras que otras solo necesitan ver o hacer una copia. En Florida, puede solicitar certificados de defunción <b>con</b> o <b>sin la causa de muerte.</b> La causa de muerte es confidencial y solo debe incluirse cuando sea necesario.</p>

    <table class="uses">
      <colgroup><col class="c1"><col class="c2"><col class="c3"><col></colgroup>
      <thead><tr><th>Uso</th><th>¿Original Necesario?</th><th>¿Con Causa?</th><th>Cantidad Sugerida</th></tr></thead>
      <tbody>
        <tr><td>Reclamos de Seguro de Vida</td><td><span class="cb">Sí</span></td><td><span class="cb">Sí</span></td><td><span class="cb">1 por póliza</span></td></tr>
        <tr><td>Beneficios de Pensión o Jubilación</td><td><span class="cb">Sí</span></td><td><span class="cb">Sí</span></td><td><span class="cb">1</span></td></tr>
        <tr><td>Cuentas Bancarias</td><td><span class="cb">Generalmente No</span></td><td><span class="cb">No</span></td><td><span class="cb">0–1</span></td></tr>
        <tr><td>Cuentas de Inversión / Corretaje</td><td><span class="cb">A veces</span></td><td><span class="cb">A veces</span></td><td><span class="cb">1–2</span></td></tr>
        <tr><td>Transferencia de Título Vehicular (DMV)</td><td><span class="cb">Sí</span></td><td><span class="cb">No</span></td><td><span class="cb">1</span></td></tr>
        <tr><td>Transferencia de Propiedad / Bienes Raíces</td><td><span class="cb">Sí</span></td><td><span class="cb">No</span></td><td><span class="cb">1 por propiedad</span></td></tr>
        <tr><td>Asuntos Legales / Tribunal / Sucesiones</td><td><span class="cb">Sí</span></td><td><span class="cb">Frecuente</span></td><td><span class="cb">1–2</span></td></tr>
        <tr><td>Seguridad Social / Beneficios del Gobierno</td><td><span class="cb">No</span></td><td><span class="cb">No</span></td><td><span class="cb">0</span></td></tr>
        <tr><td>Cancelación de Pasaporte / Consulados</td><td><span class="cb">Sí</span></td><td><span class="cb">Sí</span></td><td><span class="cb">1</span></td></tr>
        <tr><td>Viaje Doméstico con Restos Cremados</td><td><span class="cb">Sí</span></td><td><span class="cb">No</span></td><td><span class="cb">1</span></td></tr>
        <tr><td>Viaje Internacional con Restos Cremados</td><td><span class="cb">Sí</span></td><td><span class="cb">A veces</span></td><td><span class="cb">1</span></td></tr>
        <tr><td>Traslado Doméstico de Restos</td><td><span class="cb">Sí</span></td><td><span class="cb">No</span></td><td><span class="cb">1</span></td></tr>
        <tr><td>Traslado Internacional de Restos</td><td><span class="cb">Sí</span></td><td><span class="cb">Sí</span></td><td><span class="cb">1</span></td></tr>
        <tr><td>Tarjetas de Crédito / Servicios Públicos</td><td><span class="cb">Generalmente No</span></td><td><span class="cb">No</span></td><td><span class="cb">0</span></td></tr>
        <tr><td>Copia Personal / Para Tranquilidad</td><td><span class="cb">Opcional</span></td><td><span class="cb">Opcional</span></td><td><span class="cb">1</span></td></tr>
      </tbody>
    </table>

    <p class="sub">PRECIOS (CONDADO DE MIAMI-DADE):</p>
    <p class="para">El primer certificado de defunción certificado cuesta <b>$20</b> y cada copia adicional cuesta <b>$16.</b></p>
    <p class="para" style="margin-top:8px">Si va a <b>viajar dentro o fuera del país con restos cremados,</b> normalmente se requiere al menos una copia certificada. Algunos países pueden requerir el certificado <b>con causa de muerte.</b> Nos comunicaremos con el consulado del país de destino para confirmar los requisitos específicos para el traslado.</p>

    <p class="sub">TENGA EN CUENTA QUE:</p>
    <p class="para"><b>Otros condados pueden tener precios diferentes</b> para los certificados de defunción. Le informaremos del costo exacto según el lugar de fallecimiento.</p>
    <p class="para" style="margin-top:8px"><b>La mayoría de las familias solicitan entre 4 y 8 copias certificadas.</b> Es común pedir una combinación — por ejemplo, 2 con causa y 4 sin causa. Es más conveniente y económico solicitarlas en el momento del servicio. Si tiene dudas, estamos aquí para guiarle.</p>

    <div class="sec__head" style="margin-top:9px;width:486px"><h2>¿CUÁNTAS COPIAS CERTIFICADAS DESEA SOLICITAR?</h2></div>
    <p class="blanks">____________Con Causa de Muerte<br>____________ Sin Causa de Muerte</p>

    <div class="sec__head" style="margin-top:6px;width:486px"><h2>¿PREGUNTAS? ESTAMOS AQUÍ PARA USTED</h2></div>
    <div class="contact">
      <div class="contact__list">
        <div class="contact__phone">
          <svg width="7" height="10" viewBox="0 0 7 10" aria-hidden="true"><rect x=".5" y=".5" width="6" height="9" rx="1" fill="none" stroke="#4c7d9c"/><line x1="2.5" y1="8" x2="4.5" y2="8" stroke="#4c7d9c"/></svg>
          (305) 555-0148
        </div>
        <div class="contact__mail">
          <svg width="8" height="8" viewBox="0 0 10 10" style="margin-top:22px" aria-hidden="true"><circle cx="5" cy="5" r="4.4" fill="none" stroke="#4c7d9c" stroke-width=".8"/><ellipse cx="5" cy="5" rx="2" ry="4.4" fill="none" stroke="#4c7d9c" stroke-width=".8"/><line x1=".6" y1="5" x2="9.4" y2="5" stroke="#4c7d9c" stroke-width=".8"/></svg>
          <ul>
            <li>kendall@hartwellfuneral.com</li>
            <li>midtown@hartwellfuneral.com</li>
            <li>coralgables@hartwellfuneral.com</li>
            <li>preplanning@hartwellfuneral.com</li>
          </ul>
        </div>
      </div>
      <p class="contact__line">Sirviendo al condado de Miami-Dade con cuidado,<br>dignidad y apoyo por más de 90 años.</p>
    </div>
  </div>
</section>

</body>
</html>
```